CEO Survey Report Landing Page - lead response

Looking for responsive design landing page done in modern elegant style that will appeal to the top executive (CEO) of big businesses. This page should collect first name, last name, business email and have download button. we require source file in both adobe photoshop psd and indesign (idd).

Example of landing page: https://blog.plintrova.com/post/503817264915/how-to-design-an-optimized-ebook-landing-page (see attachments for more examples)

Target Market(s)

CEO - top executive of US business between 100 million to 1 billion a year in revenue

Number of Pages Required

1 page

Font styles to use
Sans Serif

Colors
0692cd
ffffff
f78f20
9bcb3b

Requirements
Must have
• place the copy text given in the doc on the page. we are focusing on 1. meaning of copy text being powerful and easy to understand. 2. a way to highlight the 3 numeric values with text . 3. clear call to action.
Nice to have
• idea 1. see the 3 numbers with a graphic. consider for example like put each number in a circle with label below.
• optional idea 2. perhaps consider an elegant business info-graphic look
• optional idea 3. as an option consider screened gradient color in blue /green or photo with translucent layer - behind make white / light gray main area where have copy etc.
Should not have
• do NOT make this look like a regular website. see the plintrova link and sample reference of landing page designs. it should be a landing page with clear easy elegant form with a lot of clear space.
• have cluttered looks. photo images of people in the foreground etc that distracts is bad. a screened back photo in the background is fine.

```html
<!DOCTYPE html>
<html lang="en">
<head>
<meta charset="utf-8">
<title>2018 CEO Cloud Survey</title>
<link href="https://fonts.googleapis.com/css2?family=Roboto:wght@300;400;500&display=swap" rel="stylesheet">
<style>
  :root {
    --brand-blue: #0b9bf7;
    --button-blue: #4cb8fb;
    --ink-grey: #5b5f66;
    --label-grey: #6d7178;
    --white: #ffffff;
    --input-border: #7cc4f5;
    --card-shadow: #b9bcc2;
    --bar-green: #9bc11a;
    --bar-sky: #7accdf;
    --bar-yellow: #edd100;
    --bar-orange: #f08400;
    --bar-purple: #7f347c;
    --bar-blue: #14a0dc;
  }
  * { box-sizing: border-box; margin: 0; padding: 0; }
  html, body { width: 1200px; height: 3309px; overflow: hidden; background: var(--white); }
  body { position: relative; font-family: 'Roboto', Arial, sans-serif; color: var(--ink-grey); }
  h1, h2, h3 { font-weight: 400; }

  .hero { position: absolute; left: 0; top: 380px; width: 1200px; height: 593px; }
  .hero-photo { position: absolute; inset: 0;
    background: linear-gradient(100deg, #eef1f5 0%, #e3e8ee 40%, #cfd6df 70%, #b9c2cf 100%); }
  .hero-headline { position: absolute; top: 228px; width: 100%; text-align: center;
    font-size: 53px; font-weight: 400; color: var(--ink-grey); }
  .hero-sub { position: absolute; top: 300px; width: 100%; text-align: center;
    font-size: 35px; font-weight: 400; color: var(--brand-blue); }

  .signup-band { position: absolute; left: 0; top: 973px; width: 1200px; height: 417px; background: var(--brand-blue); }
  .signup-claim { position: absolute; left: 75px; top: 156px; color: var(--white);
    font-size: 44px; line-height: 56px; font-weight: 400; }
  .signup-form { position: absolute; left: 719px; top: 927px; width: 448px; height: 399px;
    background: var(--white); box-shadow: 0 2px 6px rgba(0,0,0,.12); }
  .field { position: absolute; left: 27px; width: 337px; height: 57px; border: 2px solid var(--input-border);
    font-size: 24px; color: #8a8e94; padding: 13px 0 0 20px; }
  .field-first { top: 55px; } .field-last { top: 127px; } .field-email { top: 200px; }
  .submit { position: absolute; left: 27px; top: 277px; width: 399px; height: 66px;
    background: var(--button-blue); color: var(--white); font-size: 25px; text-align: center; line-height: 66px; }

  .things { position: absolute; left: 0; top: 1390px; width: 1200px; height: 408px; }
  .things-photo { position: absolute; inset: 0;
    background: linear-gradient(120deg, #c9d3df 0%, #e4eaf0 35%, #d6e0ea 65%, #bccbdb 100%); }
  .things-title { position: absolute; top: 102px; width: 100%; text-align: center;
    font-size: 60px; font-weight: 400; color: var(--ink-grey); }
  .pill { position: absolute; top: 203px; height: 66px; line-height: 66px; text-align: center;
    background: var(--button-blue); color: var(--white); font-size: 29px; }
  .pill-pitfalls { left: 329px; width: 242px; }
  .pill-watch { left: 587px; width: 295px; }

  .report-band { position: absolute; left: 0; top: 1798px; width: 1200px; height: 415px; background: var(--brand-blue); color: var(--white); }
  .report-icon { position: absolute; left: 176px; top: 108px; }
  .report-title { position: absolute; left: 238px; top: 106px; font-size: 33px; font-weight: 500; }
  .report-sub { position: absolute; left: 240px; top: 152px; font-size: 32px; font-weight: 300; }
  .report-button { position: absolute; left: 412px; top: 225px; width: 402px; height: 66px; line-height: 66px;
    text-align: center; background: var(--button-blue); font-size: 29px; }

  .concerns { position: absolute; left: 0; top: 2213px; width: 1200px; height: 401px; }
  .concerns-photo { position: absolute; inset: 0;
    background: linear-gradient(90deg, #dfe6f2 0%, #eef2f8 45%, #c8d3ea 75%, #d7def0 100%); }
  .concerns-title { position: absolute; left: 146px; top: 168px; font-size: 60px; font-weight: 400; color: var(--brand-blue); }

  .chart-card { position: absolute; left: 119px; top: 2592px; width: 991px; height: 463px;
    background: var(--white); box-shadow: 3px 3px 0 var(--card-shadow); }
  .chart-row { position: absolute; left: 38px; height: 30px; width: 940px; }
  .chart-label { position: absolute; left: 0; top: 0; font-size: 24px; color: var(--label-grey); }
  .chart-bar { position: absolute; left: 425px; top: 2px; height: 22px; }
  .chart-value { position: absolute; top: 0; font-size: 22px; color: var(--label-grey); }
</style>
</head>
<body>
  <section class="hero">
    <div class="hero-photo" role="img" aria-label="Softly screened photo of business executives reviewing documents at a desk"></div>
    <h1 class="hero-headline">John achieve your objectives easier.</h1>
    <p class="hero-sub">See what other CEOs are saying about Cloud.</p>
  </section>

  <section class="signup-band">
    <p class="signup-claim">5000 CEOs<br>Of US Mid-Sized Companies</p>
  </section>
  <form class="signup-form">
    <div class="field field-first">First Name</div>
    <div class="field field-last">Last Name</div>
    <div class="field field-email">Business E-mail</div>
    <div class="submit">Get the 2018 CEO Cloud Survey</div>
  </form>

  <section class="things">
    <div class="things-photo" role="img" aria-label="Screened photo of a glass office tower seen from below"></div>
    <h2 class="things-title">6 Things To Know</h2>
    <div class="pill pill-pitfalls">Cloud Pitfalls</div>
    <div class="pill pill-watch">Areas To Watch Out</div>
  </section>

  <section class="report-band">
    <svg class="report-icon" width="38" height="38" viewBox="0 0 38 38" aria-hidden="true">
      <circle cx="19" cy="19" r="18" fill="#ffffff"/>
      <path d="M10 19.5 L16.5 26 L28 13" fill="none" stroke="#0b9bf7" stroke-width="4" stroke-linecap="round" stroke-linejoin="round"/>
    </svg>
    <h3 class="report-title">6 Recommendations</h3>
    <p class="report-sub">A quick 10 minute read to succeed better with Cloud.</p>
    <div class="report-button">Download the report now!</div>
  </section>

  <section class="concerns">
    <div class="concerns-photo" role="img" aria-label="Screened stock chart backdrop with a magnifying glass over bar graphs"></div>
    <h2 class="concerns-title">Cloud Concerns</h2>
  </section>

  <div class="chart-card">
    <div class="chart-row" style="top:84px">
      <span class="chart-label">Tax on executive time to oversee</span>
      <span class="chart-bar" style="width:300px;background:var(--bar-green)"></span>
      <span class="chart-value" style="left:747px">53%</span>
    </div>
    <div class="chart-row" style="top:141px">
      <span class="chart-label">Worry about team execution</span>
      <span class="chart-bar" style="width:371px;background:var(--bar-sky)"></span>
      <span class="chart-value" style="left:814px">65%</span>
    </div>
    <div class="chart-row" style="top:198px">
      <span class="chart-label">Cost</span>
      <span class="chart-bar" style="width:401px;background:var(--bar-yellow)"></span>
      <span class="chart-value" style="left:847px">70%</span>
    </div>
    <div class="chart-row" style="top:255px">
      <span class="chart-label">Security</span>
      <span class="chart-bar" style="width:450px;background:var(--bar-orange)"></span>
      <span class="chart-value" style="left:893px">81%</span>
    </div>
    <div class="chart-row" style="top:312px">
      <span class="chart-label">Keep pace with Cloud evolution</span>
      <span class="chart-bar" style="width:324px;background:var(--bar-purple)"></span>
      <span class="chart-value" style="left:770px">57%</span>
    </div>
    <div class="chart-row" style="top:369px">
      <span class="chart-label">Retention of Cloud talent</span>
      <span class="chart-bar" style="width:146px;background:var(--bar-blue)"></span>
      <span class="chart-value" style="left:589px">20%</span>
    </div>
  </div>
</body>
</html>
```